Towel Company Needs A Product Label

My client is looking for a phenomenal label to used their flagship product. The product is a durable, reusable, rinsable paper towel. We are marketing as a luxury brand that rivals other top paper towel companies. Our main colors are black red and white. The label will be a sticker to be placed on the plastic wrapping of each roll.

The clients would like to maintain to the current font (fh_script) and color scheme, especially the white background, but we are open to a new wowing design that deviates some from the current look.

Our website in progress is www.velmi.examplestore.com.

NOTE: We've attached a mock-up label below that was created locally. Your design doesn't need to be based off it that one, it was uploaded to give you an idea of what we are looking to upgrade. We are wanting something more creative that'll stand out to customers.

Target Market(s)

upper middle class, homemakers

Industry/Entity Type

Cleaning Product

Font styles to use
Other font styles liked:
• fh_script

Colors
ec1f27
ffffff
000000

Requirements
Must have
• velmi name , white black and red color scheme, "reinventing the way you clean" tag line, "75 count" , "11"x16"", www.velmi75.example
Nice to have
• same (fh_script) font

```html
<!DOCTYPE html>
<html lang="en">
<head>
<meta charset="UTF-8">
<title>Velmi75 Roll Label</title>
<link href="https://fonts.googleapis.com/css2?family=Montserrat:wght@400;600;700&display=swap" rel="stylesheet">
<style>
  :root {
    --ink: #000000;
    --paper: #ffffff;
    --brand-red: #ec1f27;
    --muted: #9a9a9a;
  }
  * { margin: 0; padding: 0; box-sizing: border-box; }
  html, body {
    width: 800px;
    height: 1200px;
    overflow: hidden;
    background: var(--paper);
  }
  .canvas {
    width: 800px;
    height: 1200px;
    display: flex;
    align-items: center;
    justify-content: center;
    background: var(--paper);
  }
  .label {
    width: 560px;
    height: 660px;
    background: var(--ink);
    padding: 18px;
  }
  .label__frame {
    width: 100%;
    height: 100%;
    border: 2px solid var(--paper);
    display: flex;
    flex-direction: column;
    align-items: center;
    justify-content: center;
    font-family: "Montserrat", sans-serif;
    color: var(--paper);
    text-align: center;
  }
  .brand-name {
    font-family: "Montserrat", sans-serif;
    font-weight: 600;
    font-size: 78px;
    color: var(--brand-red);
    letter-spacing: 1px;
    margin-bottom: 70px;
  }
  .tagline__lead {
    font-weight: 700;
    font-size: 34px;
    letter-spacing: 3px;
  }
  .tagline__sub {
    font-weight: 400;
    font-size: 14px;
    letter-spacing: 3px;
    margin-top: 8px;
  }
  .specs {
    margin-top: 70px;
    font-weight: 400;
    font-size: 22px;
    letter-spacing: 2px;
    display: flex;
    align-items: center;
    gap: 16px;
  }
  .specs__dot {
    width: 10px;
    height: 10px;
    border-radius: 50%;
    background: var(--brand-red);
  }
  .site-url {
    margin-top: 28px;
    font-size: 12px;
    letter-spacing: 1px;
    color: var(--muted);
  }
</style>
</head>
<body>
  <main class="canvas">
    <section class="label">
      <div class="label__frame">
        <div class="brand-name">Velmi75</div>
        <div class="tagline">
          <p class="tagline__lead">REINVENTING</p>
          <p class="tagline__sub">THE WAY YOU CLEAN</p>
        </div>
        <div class="specs">
          <span class="specs__count">75 COUNT</span>
          <span class="specs__dot"></span>
          <span class="specs__size">11" x 16"</span>
        </div>
        <p class="site-url">www.velmi75.example</p>
      </div>
    </section>
  </main>
</body>
</html>
```